People/Expertise finder to associate people to experts, services and products

Design a mock-up for a people finder/expertise finder system. The people/expertise finder project is targeting to relate people to experts, countries and core operations. We are expecting the final UI to be responsive. The styleguide that is followed in the enterprise is attached for reference. further documents outlining the vision is also attached. Based on queries kindly use the crew deck profile as an example of profile page. People will search using the enterprise search on names, skills etc to find matching people.

Logo Text

People Finder

Number of Pages Required

3 page

Requirements
Must have
• The UI should be aesthetically good and should bring in the industry standards

```html
<!DOCTYPE html>
<html lang="en">
<head>
<meta charset="utf-8">
<title>Find People – Profile</title>
<link href="https://fonts.googleapis.com/css2?family=Open+Sans:wght@400;600;700&display=swap" rel="stylesheet">
<style>
:root{
  --navy:#0f2540;
  --page:#ececec;
  --card:#ffffff;
  --ink:#1b1b1b;
  --muted:#6f6f6f;
  --link:#1a73d6;
  --line:#e6e6e6;
  --gold:#f5b826;
  --badge:#e8336b;
}
*{box-sizing:border-box;margin:0;padding:0}
html,body{width:1111px;height:1200px;overflow:hidden}
body{background:var(--page);font-family:"Open Sans",Arial,sans-serif;color:var(--ink);font-size:10px;position:relative}
a{color:var(--link);text-decoration:none}

.topbar{position:absolute;left:0;top:0;width:1111px;height:48px;background:var(--navy);border-bottom:2px solid #5d6b7b}
.brand{position:absolute;left:135px;top:10px;display:flex;align-items:center;gap:9px;color:#fff;font-size:14px;font-weight:600;letter-spacing:.2px}
.brand-dot{width:24px;height:24px;border-radius:50%;background:#fff}
.search{position:absolute;left:545px;top:10px;width:211px;height:28px;border:1px solid #c6ccd3;border-radius:2px;color:#a9b2bd;font-size:8px;padding:8px 15px;letter-spacing:.5px}
.search svg{position:absolute;right:11px;top:7px}
.ico{position:absolute;top:15px}
.ico .count{position:absolute;right:-6px;top:-5px;width:10px;height:10px;border-radius:50%;background:var(--badge);color:#fff;font-size:6.5px;line-height:10px;text-align:center}
.user{position:absolute;left:864px;top:10px;display:flex;align-items:center;gap:8px;color:#fff;font-size:11px}
.avatar{border-radius:50%;background:radial-gradient(circle at 50% 40%,#e6c4ad,#a97f68 70%,#7b5a4a)}

.sidenav{position:absolute;left:133px;top:70px;width:149px;background:var(--card)}
.sidenav li{list-style:none;border-bottom:1px solid var(--line);padding:0 15px;font-size:9.5px;color:#333;line-height:16.5px;display:flex;align-items:center;height:41.5px}
.sidenav li.tall{height:59px}
.sidenav li.active{color:var(--link)}

.card{position:absolute;background:var(--card)}
.profile{left:297px;top:70px;width:490px;height:134px}
.profile .photo{position:absolute;left:22px;top:22px;width:49px;height:49px}
.name{position:absolute;left:94px;top:21px;font-size:11.5px;font-weight:600;color:#333;display:flex;align-items:center;gap:10px;letter-spacing:.2px}
.gold{background:var(--gold);color:#fff;font-size:5.5px;font-weight:700;padding:1px 4px;border-radius:1px;letter-spacing:.5px}
.dept{position:absolute;left:95px;top:39px;font-size:8px;color:var(--muted)}
.divider{position:absolute;left:94px;top:57px;width:373px;height:1px;background:var(--line)}
.social{position:absolute;left:94px;top:64px;display:flex;gap:12px;font-size:8.5px;font-weight:600;color:var(--link)}
.edit-btn{position:absolute;left:379px;top:22px;width:88px;height:20px;background:var(--link);color:#fff;font-size:8.5px;text-align:center;line-height:20px;border-radius:1px;letter-spacing:.2px}
.contact{position:absolute;top:89px;font-size:8.3px}
.contact b{display:block;font-size:6px;color:#888;font-weight:600;letter-spacing:.6px;margin-bottom:3px}

.section-head{height:50px;border-bottom:1px solid var(--line);display:flex;align-items:center;justify-content:space-between;padding:0 22px 0 21px}
.section-head h2{font-size:12px;font-weight:600}
.edit{color:var(--link);font-size:10px;display:flex;align-items:center;gap:5px}
.spec{left:297px;top:211px;width:490px;height:675px}
.worklist{padding:16px 21px 0}
.intro{padding:14px 21px 13px;border-bottom:1px solid var(--line);font-size:9.5px;line-height:17px}
.intro h3{font-size:10px;font-weight:600;margin-bottom:6px}
.group{padding:0 22px 0 21px}
.group h3{font-size:10px;font-weight:600;margin:13px 0 0}
.row{display:flex;justify-content:space-between;align-items:center;height:33.3px;border-bottom:1px solid var(--line);font-size:9.5px}
.row a{font-size:8.5px}

.work{left:297px;top:893px;width:490px;height:260px}
.job{display:flex;gap:14px;height:89px;border-bottom:1px solid var(--line);padding-top:1px}
.job+.job{padding-top:15px}
.logo{width:53px;height:53px;border:1px solid var(--line);display:flex;align-items:center;justify-content:center;font-size:8px;color:#555;flex:none;text-align:center}
.job h4{font-size:10.5px;font-weight:600}
.job i{display:block;font-size:8.5px;margin-top:3px}
.job small{display:block;font-size:7.5px;margin-top:4px}
.job p{font-size:9.3px;margin-top:5px}

.side{left:799px;width:178px}
.side h2{font-size:9.5px;font-weight:600;height:41px;border-bottom:1px solid var(--line);padding:0 15px;display:flex;align-items:center}
.people{padding-top:14px}
.person{display:flex;gap:10px;padding:0 14px;align-items:flex-start;line-height:1.2}
.unit .person{height:48px}
.recent .person{height:52px}
.person .avatar{width:37px;height:37px;flex:none}
.person a{font-size:8.8px;display:block;margin-top:4px}
.person span{font-size:8.3px;display:block;margin-top:4px}
.person em{font-style:normal;font-size:7.5px;color:#555;display:block;margin-top:3px}
.see-all{border-top:1px solid var(--line);text-align:right;padding:10px 15px 0;font-size:8.5px;height:35px}
</style>
</head>
<body>

<header class="topbar">
  <div class="brand"><span class="brand-dot"></span>FIND PEOPLE</div>
  <div class="search">SEARCH
    <svg width="12" height="12" viewBox="0 0 12 12"><circle cx="5" cy="5" r="4" fill="none" stroke="#c6ccd3" stroke-width="1.4"/><line x1="8" y1="8" x2="11" y2="11" stroke="#c6ccd3" stroke-width="1.4"/></svg>
  </div>
  <div class="ico" style="left:778px">
    <svg width="16" height="12" viewBox="0 0 16 12"><rect width="16" height="12" rx="1" fill="#fff"/><path d="M0 1l8 6 8-6" fill="none" stroke="var(--navy)" stroke-width="1.2"/></svg>
    <span class="count">1</span>
  </div>
  <div class="ico" style="left:809px">
    <svg width="15" height="15" viewBox="0 0 15 15"><path d="M7.5 1a4.5 4.5 0 0 1 4.5 4.5V9l2 3H1l2-3V5.5A4.5 4.5 0 0 1 7.5 1z" fill="#fff"/><circle cx="7.5" cy="13.5" r="1.5" fill="#fff"/></svg>
    <span class="count">4</span>
  </div>
  <div class="user">
    <div class="avatar" style="width:28px;height:28px" role="img" aria-label="User profile photo"></div>
    Hello Marsh
    <svg width="10" height="7" viewBox="0 0 10 7"><path d="M1 1l4 4 4-4" fill="none" stroke="#fff" stroke-width="1.8"/></svg>
  </div>
</header>

<ul class="sidenav">
  <li class="active">Contact &amp; basic Info</li>
  <li class="tall">Specialization, Skills &amp;<br>Languages</li>
  <li>Work History</li>
  <li>Project Experience</li>
  <li>Education &amp; Learning</li>
  <li>Publications &amp; Documents</li>
  <li>About Theo</li>
  <li>References</li>
</ul>

<section class="card profile">
  <div class="photo avatar" style="background:radial-gradient(circle at 50% 45%,#bdbdbd,#6d6d6d 70%,#3a3a3a)" role="img" aria-label="Profile photo of Theo Marsh"></div>
  <div class="name">THEO MARSH <span class="gold">GOLD</span></div>
  <div class="dept">Sales &amp; Marketing</div>
  <div class="divider"></div>
  <div class="social"><span>crew deck</span><span>Friendwall</span><span>Chirper</span></div>
  <a class="edit-btn" href="#">EDIT PROFILE</a>
  <div class="contact" style="left:22px"><b>PHONE</b>(+31) 555 010 238</div>
  <div class="contact" style="left:150px"><b>EMAIL</b>theo.marsh@mailbox.test</div>
  <div class="contact" style="left:299px"><b>ADDRESS</b>Kanaalstraat 12, Dorpveld</div>
</section>

<section class="card spec">
  <div class="section-head"><h2>Specialization</h2>
    <a class="edit" href="#">edit <svg width="10" height="10" viewBox="0 0 10 10"><path d="M1 9l1-3 5-5 2 2-5 5z" fill="var(--link)"/></svg></a></div>
  <div class="intro"><h3>I work on</h3>Systematic Tracking of Exchanges in Procurement (STEP) and procurement systems as well as Data Analytics</div>
  <div class="group">
    <h3>Primary Specialization</h3>
    <div class="row">IT Project Management<a href="#">10 people endorsed</a></div>
    <div class="row">Information Technology Procurement Services<a href="#">9 people endorsed</a></div>
    <div class="row">Business Processes and Systems<a href="#">8 people endorsed</a></div>
    <h3>Secondary Specialization</h3>
    <div class="row">IT Project Management<a href="#">10 people endorsed</a></div>
    <div class="row">Information Technology Procurement Services<a href="#">9 people endorsed</a></div>
    <div class="row">Business Processes and Systems<a href="#">8 people endorsed</a></div>
    <h3>Skills</h3>
    <div class="row">Business Process Reengineering<a href="#">10 people endorsed</a></div>
    <div class="row">Client Relationship Management<a href="#">9 people endorsed</a></div>
    <div class="row">Business Requirements Gathering<a href="#">8 people endorsed</a></div>
    <div class="row">Collaborative Tools<a href="#">7 people endorsed</a></div>
    <h3>Languages</h3>
    <div class="row">English<a href="#">10 people endorsed</a></div>
    <div class="row">Japanese<a href="#">9 people endorsed</a></div>
  </div>
</section>

<section class="card work">
  <div class="section-head"><h2>Work History</h2>
    <a class="edit" href="#">edit <svg width="10" height="10" viewBox="0 0 10 10"><path d="M1 9l1-3 5-5 2 2-5 5z" fill="var(--link)"/></svg></a></div>
  <div class="worklist">
    <div class="job"><div class="logo">Brightlane</div>
      <div><h4>Brightlane</h4><i>Quality Control Manager</i><small>Sept 2016 - Present</small><p>managing project, quality control, leading team, gathering project requirements</p></div></div>
    <div class="job"><div class="logo">Orchard Labs</div>
      <div><h4>Orchard Labs</h4><i>Programmer</i><small>Jan 2009 - Aug 2016</small><p>managing project, quality control, leading team, gathering project requirements</p></div></div>
  </div>
</section>

<aside class="card side unit" style="top:70px;height:335px">
  <h2>PEOPLE IN THE SAME UNIT</h2>
  <div class="people" style="height:259px">
    <div class="person"><div class="avatar" role="img" aria-label="Colleague photo"></div><div><a href="#">Nadia R. Okafor</a><span>Director</span></div></div>
    <div class="person"><div class="avatar" role="img" aria-label="Colleague photo"></div><div><a href="#">Nadia R. Okafor</a><span>Director</span></div></div>
    <div class="person"><div class="avatar" role="img" aria-label="Colleague photo"></div><div><a href="#">Nadia R. Okafor</a><span>Director</span></div></div>
    <div class="person"><div class="avatar" role="img" aria-label="Colleague photo"></div><div><a href="#">Nadia R. Okafor</a><span>Director</span></div></div>
    <div class="person"><div class="avatar" role="img" aria-label="Colleague photo"></div><div><a href="#">Nadia R. Okafor</a><span>Director</span></div></div>
  </div>
  <div class="see-all"><a href="#">see all</a></div>
</aside>

<aside class="card side recent" style="top:411px;height:350px">
  <h2>RECENTLY UPDATED PROFILES</h2>
  <div class="people" style="height:274px">
    <div class="person"><div class="avatar" role="img" aria-label="Profile photo"></div><div><a href="#">Nadia R. Okafor</a><span>Director</span><em>Oct 14, 2016 10:51</em></div></div>
    <div class="person"><div class="avatar" role="img" aria-label="Profile photo"></div><div><a href="#">Nadia R. Okafor</a><span>Director</span><em>Oct 14, 2016 10:51</em></div></div>
    <div class="person"><div class="avatar" role="img" aria-label="Profile photo"></div><div><a href="#">Nadia R. Okafor</a><span>Director</span><em>Oct 14, 2016 10:51</em></div></div>
    <div class="person"><div class="avatar" role="img" aria-label="Profile photo"></div><div><a href="#">Nadia R. Okafor</a><span>Director</span><em>Oct 14, 2016 10:51</em></div></div>
    <div class="person"><div class="avatar" role="img" aria-label="Profile photo"></div><div><a href="#">Nadia R. Okafor</a><span>Director</span><em>Oct 14, 2016 10:51</em></div></div>
  </div>
  <div class="see-all"><a href="#">see all</a></div>
</aside>

</body>
</html>
```